Landing page for a cyber security service provider called 'Lumen Grove'

The client is a new cyber security company in need of a website landing page at lumengrove.example.

Their visual identity is modern, playful, clean and uncluttered and represents innovation, connectivity and approachability.

The company logo is provided in black (attached) but the client is open to changing the colour to align with the new website design.

The landing page needs to contain:
- A call to action with a 'Get Started' button
-Links to blank 'How it works', 'Products', 'Pricing', 'About Us' and 'Contact Us' pages (that we'll fill out later)

Target Market(s)

Medium to large businesses who probably don't understand cyber / cyber security but need their business to be protected.

Industry/Entity Type

Cyber Security

Coding

Coded - Design and coding required

Number of Pages Required

1 page

Font styles to use
Sans Serif
Other font styles liked:
• Helvetica

Requirements
Nice to have
• Hero banner at the top of the landing page.
Should not have
• Should not look like a traditional cyber / cyber security design (eg no dark blue/ black, red/black colour combinations). Please no military styles (eg no shields, cannons, swords, guns)

```html
<!DOCTYPE html>
<html lang="en">
<head>
<meta charset="utf-8">
<title>Lumen Grove — Cyber Security</title>
<link href="https://fonts.googleapis.com/css2?family=Montserrat:wght@400;500;600;700&display=swap" rel="stylesheet">
<style>
:root{
  --green:#6fb52c;
  --green-dark:#5a9a1f;
  --ink:#111111;
  --text:#333333;
  --muted:#555555;
  --line:#d9d9d9;
  --white:#ffffff;
  --black:#000000;
  --panel:rgba(30,30,30,.88);
}
*{box-sizing:border-box;margin:0;padding:0}
html,body{width:1200px;height:5128px;overflow:hidden}
body{font-family:'Montserrat',sans-serif;color:var(--text);background:var(--white);position:relative}
.abs{position:absolute}
a{color:inherit;text-decoration:none}

/* header */
.site-header{position:absolute;left:0;top:0;width:1200px;height:100px;background:var(--white);z-index:5}
.brand-disc{position:absolute;left:72px;top:-60px;width:246px;height:246px;border-radius:50%;background:var(--white);display:flex;align-items:flex-end;justify-content:center;padding-bottom:78px;z-index:6}
.brand-name{font-weight:700;font-size:24px;color:var(--ink);letter-spacing:.5px;display:flex;align-items:center;gap:8px}
.brand-name .dot{width:12px;height:12px;border-radius:50%;background:var(--green)}
.main-nav{position:absolute;right:65px;top:30px;display:flex;align-items:center;gap:30px;font-size:11px;font-weight:500;color:#444;white-space:nowrap}
.main-nav .active{color:var(--green);border-bottom:2px solid var(--green);padding-bottom:8px;margin-top:10px}
.pill{display:inline-flex;align-items:center;gap:10px;border-radius:30px;font-weight:600;color:var(--white);background:var(--green);white-space:nowrap}
.main-nav .pill{height:38px;padding:0 20px;font-size:11px}

/* hero */
.hero{position:absolute;left:0;top:100px;width:1200px;height:678px;background:linear-gradient(100deg,#cfcfcf 0%,#bdbdbd 40%,#9a9a9a 65%,#d6d6d6 100%)}
.hero-panel{position:absolute;left:0;top:168px;width:650px;height:357px;background:var(--panel);clip-path:polygon(0 0,100% 0,72% 100%,0 100%)}
.hero h1{position:absolute;left:68px;top:210px;font-size:50px;font-weight:500;color:var(--white);white-space:nowrap}
.hero p{position:absolute;left:70px;top:298px;width:470px;font-size:13px;line-height:25px;color:#eee}
.hero .pill{position:absolute;left:70px;top:388px;height:52px;padding:0 18px 0 30px;font-size:14px}
.arrow-dot{width:22px;height:22px;border-radius:50%;background:var(--white);display:inline-flex;align-items:center;justify-content:center}
.arrow-dot.dark{background:var(--black)}
.slider-dots{position:absolute;left:572px;top:612px;display:flex;gap:5px}
.slider-dots span{width:10px;height:10px;border-radius:50%;background:rgba(255,255,255,.6)}
.slider-dots span:first-child{background:var(--white)}

/* common headings */
.eyebrow{color:var(--green);font-weight:600;font-size:22px;display:flex;align-items:center;gap:10px}
.eyebrow .rule{display:inline-block;width:55px;height:2px;background:var(--green)}
.center{justify-content:center}
.section-title{font-weight:600;color:var(--ink);font-size:42px}
.lead{font-size:13px;line-height:27px;color:var(--text)}

/* about */
.about-art{position:absolute;left:160px;top:910px;width:360px;height:340px;border-radius:50%;background:radial-gradient(circle,#e8e4e0 0%,#c9b9ac 45%,#ffffff 72%)}
.about-copy{position:absolute;left:596px;top:898px;width:440px}
.about-copy .eyebrow{font-size:20px}
.about-copy h2{font-size:36px;font-weight:600;color:var(--ink);margin-top:8px}
.about-copy .lead{margin-top:24px}
.small-pill{height:42px;padding:0 10px 0 22px;font-size:12px}

/* steps */
.steps{position:absolute;left:68px;top:1580px;display:flex;gap:27px}
.step-card{width:246px;height:348px;background:var(--white);box-shadow:0 2px 10px rgba(0,0,0,.14);border-radius:4px;position:relative;text-align:center;padding-top:72px}
.step-tab{position:absolute;left:50%;top:0;transform:translateX(-50%);background:var(--black);color:var(--white);font-size:17px;font-weight:500;width:128px;height:30px;line-height:30px;border-radius:0 0 14px 14px}
.step-icon{width:86px;height:86px;margin:0 auto;border-radius:50%;border:3px solid var(--green);display:flex;align-items:center;justify-content:center}
.step-icon i{width:66px;height:66px;border-radius:50%;background:var(--green);display:flex;align-items:center;justify-content:center}
.step-card h3{font-size:16px;font-weight:600;color:var(--ink);margin-top:20px;line-height:20px;padding:0 12px}
.step-card p{font-size:15px;line-height:22px;color:var(--muted);margin:16px auto 0;width:190px}

/* products */
.product-card{position:absolute;width:520px;height:454px;background:var(--white);box-shadow:0 2px 10px rgba(0,0,0,.14);text-align:center}
.product-media{height:226px}
.product-card h3{color:var(--green);font-weight:500;font-size:24px;margin-top:26px}
.product-card h4{color:var(--ink);font-weight:600;font-size:17px;margin-top:8px}
.product-card p{font-size:11px;line-height:21px;color:var(--muted);width:460px;margin:14px auto 0}
.product-card .pill{height:32px;padding:0 6px 0 18px;font-size:11px;margin-top:18px;gap:8px}
.product-card .arrow-dot{width:16px;height:16px}
.view-more{position:absolute;left:490px;top:3258px;width:220px;height:64px;border-radius:32px;background:var(--black);color:var(--white);font-weight:600;font-size:18px;display:flex;align-items:center;justify-content:center;gap:16px}

/* pricing */
.price-card{position:absolute;top:3568px;width:300px;height:417px;background:var(--white);box-shadow:0 2px 10px rgba(0,0,0,.14);text-align:center}
.price-head{height:122px;background:var(--green);color:var(--white);padding-top:30px}
.price-head strong{display:block;font-size:32px;font-weight:600}
.price-head span{font-size:20px}
.price-card ul{list-style:none;text-align:left;padding:26px 0 0 50px}
.price-card li{display:flex;align-items:center;gap:12px;font-size:13px;color:var(--text);height:39px}
.tick{width:26px;height:26px;border-radius:50%;border:1.5px solid var(--green);display:flex;align-items:center;justify-content:center;flex:none}
.price-card .pill{height:46px;width:200px;justify-content:center;font-size:15px;margin-top:18px}
.price-card.featured{background:var(--black)}
.price-card.featured .price-head{background:var(--black)}
.price-card.featured li{color:var(--white)}
.price-card.featured .tick{border-color:var(--white)}

/* contact */
.contact-copy{position:absolute;left:130px;top:4110px;width:450px}
.contact-copy .eyebrow{font-size:20px}
.contact-copy h2{font-size:32px;font-weight:600;color:var(--ink);margin-top:6px}
.contact-copy .lead{margin-top:18px;font-size:13px;line-height:27px}
.field{position:absolute;height:42px;border:1px solid #e3e3e3;box-shadow:0 1px 4px rgba(0,0,0,.08);font-size:10px;color:#888;padding:14px 18px;background:var(--white)}
.contact-media{position:absolute;left:622px;top:4205px;width:383px;height:336px;border-radius:14px;background:linear-gradient(160deg,#1c2a3a 0%,#5a7590 50%,#22303f 100%)}
.dot-grid{position:absolute;left:943px;top:4148px;display:grid;grid-template-columns:repeat(6,10px);gap:16px 14px}
.dot-grid span{width:8px;height:8px;border-radius:50%;background:var(--green)}
.dot-grid span.off{background:transparent}

/* footer */
.site-footer{position:absolute;left:0;top:4668px;width:1200px;height:460px;background:var(--black);color:var(--white)}
.f-line{position:absolute;height:1px;background:#444}
.f-links{position:absolute;top:170px;display:flex;align-items:center;gap:30px;font-size:13px;font-weight:500}
.f-links .bullet{width:9px;height:9px;border-radius:50%;background:var(--green)}
.f-brand{position:absolute;left:500px;top:150px;width:200px;text-align:center;font-size:26px;font-weight:700;color:var(--white)}
.f-contacts{position:absolute;left:68px;top:272px;display:flex;gap:0}
.f-item{display:flex;align-items:center;gap:14px;width:280px}
.f-item:nth-child(3),.f-item:nth-child(4){width:290px}
.f-icon{width:64px;height:64px;border-radius:50%;background:var(--white);display:flex;align-items:center;justify-content:center;flex:none}
.f-item b{display:block;color:var(--green);font-weight:500;font-size:16px}
.f-item small{font-size:12px;color:var(--white)}
.copyright{position:absolute;left:0;top:412px;width:1200px;text-align:center;font-size:11px}
.to-top{position:absolute;left:1096px;top:404px;width:28px;height:28px;border-radius:50%;background:var(--white);display:flex;align-items:center;justify-content:center}
</style>
</head>
<body>

<header class="site-header">
  <div class="brand-disc"><span class="brand-name"><span class="dot"></span>Lumen Grove</span></div>
  <nav class="main-nav">
    <a class="active" href="#">HOME</a>
    <a href="#">ABOUT US</a>
    <a href="#">HOW IT WORKS</a>
    <a href="#">PRODUCTS</a>
    <a href="#">PRICING</a>
    <a class="pill" href="#">CONTACT US</a>
  </nav>
</header>

<section class="hero">
  <div class="abs" role="img" aria-label="Hands typing on a laptop keyboard with glowing security icons floating above" style="left:560px;top:0;width:640px;height:678px;background:radial-gradient(circle at 45% 40%,#f2f4f6 0%,#b9bcc0 45%,#8f8f8f 100%)"></div>
  <div class="hero-panel"></div>
  <h1>Welcome to Lumen Grove</h1>
  <p>Lorem ipsum dolor sit amet, consectetur adipiscing elit, sed do us mod tempor incididunt ut labore et dolore magna aliqua.</p>
  <a class="pill" href="#">GET STARTED <span class="arrow-dot dark"><svg width="10" height="10" viewBox="0 0 10 10"><path d="M3 2l3 3-3 3" stroke="#fff" stroke-width="1.8" fill="none"/></svg></span></a>
  <div class="slider-dots"><span></span><span></span><span></span><span></span></div>
</section>

<section>
  <div class="about-art" role="img" aria-label="Connected network illustration filled with a city photograph"></div>
  <div class="about-copy">
    <div class="eyebrow">Who We Are <span class="rule"></span></div>
    <h2>About Lumen Grove</h2>
    <p class="lead">Lorem ipsum dolor sit amet, consectetur adipiscing elit. Nunc et urna ut libero dignissim faucibus a sit amet sapien. Donec condimentum massa sem, ac fermentum magna tincidunt et. Ut tortor est, imperdiet quis nulla, fringilla porttitor lectus. Sed euismod leo et est imperdiet, ut luctus nisi imperdiet. Donec dictum vitae mauris vitae rutrum.</p>
    <a class="pill small-pill" href="#" style="margin-top:30px">READ MORE <span class="arrow-dot"><svg width="10" height="10" viewBox="0 0 10 10"><path d="M3 2l3 3-3 3" stroke="#6fb52c" stroke-width="1.8" fill="none"/></svg></span></a>
  </div>
</section>

<section>
  <div class="abs eyebrow center" style="left:0;top:1375px;width:1200px"><span class="rule"></span>Cyber Security<span class="rule"></span></div>
  <h2 class="abs section-title" style="left:0;top:1410px;width:1200px;text-align:center;font-size:46px">How It Works?</h2>
  <p class="abs lead" style="left:160px;top:1482px;width:880px;text-align:center">Lorem ipsum dolor sit amet, consectetur adipiscing elit. Nunc et urna ut libero dignissim faucibus a sit amet sapien. Donec condimentum massa sem, ac fermentum magna tincidunt et. Ut tortor est, imperdiet quis nulla quis.</p>
  <div class="steps">
    <div class="step-card"><span class="step-tab">Step 1</span>
      <div class="step-icon"><i><svg width="30" height="34" viewBox="0 0 30 34"><path d="M15 2c2 6 10 10 10 19a10 10 0 0 1-20 0c0-5 3-8 5-10 0 4 2 6 4 6-1-6 1-11 1-15z" fill="#fff"/></svg></i></div>
      <h3>Firewalls</h3><p>Lorem ipsum dolor sit amet, consectetur</p></div>
    <div class="step-card"><span class="step-tab">Step 2</span>
      <div class="step-icon"><i><svg width="30" height="32" viewBox="0 0 30 32"><rect x="5" y="14" width="20" height="15" rx="2" fill="#fff"/><path d="M9 14V9a6 6 0 0 1 12 0v5" stroke="#fff" stroke-width="3" fill="none"/></svg></i></div>
      <h3>Encryption</h3><p>Lorem ipsum dolor sit amet, consectetur</p></div>
    <div class="step-card"><span class="step-tab">Step 3</span>
      <div class="step-icon"><i><svg width="32" height="30" viewBox="0 0 32 30"><rect x="3" y="4" width="26" height="20" rx="2" stroke="#fff" stroke-width="2.5" fill="none"/><path d="M10 14l4 4 8-8" stroke="#fff" stroke-width="3" fill="none"/></svg></i></div>
      <h3>Antivirus and<br>Anti-malware Software</h3><p>Lorem ipsum dolor sit amet, consectetur</p></div>
    <div class="step-card"><span class="step-tab">Step 4</span>
      <div class="step-icon"><i><svg width="32" height="32" viewBox="0 0 32 32"><circle cx="13" cy="13" r="9" stroke="#fff" stroke-width="3" fill="none"/><path d="M20 20l8 8" stroke="#fff" stroke-width="4"/></svg></i></div>
      <h3>Intrusion Detection and Prevention Systems (IDPS)</h3><p>Lorem ipsum dolor sit amet, consectetur</p></div>
  </div>
</section>

<section>
  <div class="abs eyebrow center" style="left:0;top:2066px;width:1200px"><span class="rule"></span>Products<span class="rule"></span></div>
  <h2 class="abs section-title" style="left:0;top:2100px;width:1200px;text-align:center;font-size:40px">Cyber Security Products</h2>
  <p class="abs lead" style="left:160px;top:2174px;width:880px;text-align:center">Lorem ipsum dolor sit amet, consectetur adipiscing elit. Nunc et urna ut libero dignissim faucibus a sit amet sapien. Donec condimentum massa sem, ac fermentum magna tincidunt et. Ut tortor est, imperdiet quis nulla quis.</p>

  <article class="product-card" style="left:68px;top:2276px">
    <div class="product-media" role="img" aria-label="Glowing hand print scan in front of a hooded figure on a dark blue network background" style="background:radial-gradient(circle at 30% 50%,#3aa0f0 0%,#0f3c7a 40%,#071a33 100%)"></div>
    <h3>PRODUCT 1</h3><h4>Lorem Ipsum Dolor sit ament</h4>
    <p>Lorem ipsum dolor sit amet, consectetur adipiscing elit. Praesent erat sem, placerat at placerat a, facilisis eget mauris.</p>
    <a class="pill" href="#">READ MORE <span class="arrow-dot"><svg width="8" height="8" viewBox="0 0 10 10"><path d="M3 2l3 3-3 3" stroke="#6fb52c" stroke-width="2" fill="none"/></svg></span></a>
  </article>
  <article class="product-card" style="left:614px;top:2276px">
    <div class="product-media" role="img" aria-label="Glowing sphere of binary code surrounded by blue light" style="background:radial-gradient(circle at 50% 55%,#cfeeff 0%,#3d8fc0 35%,#0b2236 100%)"></div>
    <h3>PRODUCT 2</h3><h4>Lorem Ipsum Dolor sit ament</h4>
    <p>Lorem ipsum dolor sit amet, consectetur adipiscing elit. Praesent erat sem, placerat at placerat a, facilisis eget mauris.</p>
    <a class="pill" href="#">READ MORE <span class="arrow-dot"><svg width="8" height="8" viewBox="0 0 10 10"><path d="M3 2l3 3-3 3" stroke="#6fb52c" stroke-width="2" fill="none"/></svg></span></a>
  </article>
  <article class="product-card" style="left:68px;top:2750px">
    <div class="product-media" role="img" aria-label="Hands holding a tablet with a glowing padlock hologram" style="background:radial-gradient(circle at 50% 45%,#9ed6f5 0%,#3a6c90 40%,#2a2522 100%)"></div>
    <h3>PRODUCT 3</h3><h4>Lorem Ipsum Dolor sit ament</h4>
    <p>Lorem ipsum dolor sit amet, consectetur adipiscing elit. Praesent erat sem, placerat at placerat a, facilisis eget mauris.</p>
    <a class="pill" href="#">READ MORE <span class="arrow-dot"><svg width="8" height="8" viewBox="0 0 10 10"><path d="M3 2l3 3-3 3" stroke="#6fb52c" stroke-width="2" fill="none"/></svg></span></a>
  </article>
  <article class="product-card" style="left:614px;top:2750px">
    <div class="product-media" role="img" aria-label="Silhouetted person facing a large bright data centre screen" style="background:radial-gradient(circle at 50% 40%,#e5f3ff 0%,#6f9cc2 35%,#1b2c3d 100%)"></div>
    <h3>PRODUCT 4</h3><h4>Lorem Ipsum Dolor sit ament</h4>
    <p>Lorem ipsum dolor sit amet, consectetur adipiscing elit. Praesent erat sem, placerat at placerat a, facilisis eget mauris.</p>
    <a class="pill" href="#">READ MORE <span class="arrow-dot"><svg width="8" height="8" viewBox="0 0 10 10"><path d="M3 2l3 3-3 3" stroke="#6fb52c" stroke-width="2" fill="none"/></svg></span></a>
  </article>
  <a class="view-more" href="#">VIEW MORE <span class="arrow-dot"><svg width="10" height="10" viewBox="0 0 10 10"><path d="M3 2l3 3-3 3" stroke="#000" stroke-width="1.8" fill="none"/></svg></span></a>
</section>

<section>
  <div class="abs eyebrow center" style="left:0;top:3442px;width:1200px"><span class="rule" style="width:110px"></span>Pricing<span class="rule" style="width:110px"></span></div>
  <h2 class="abs section-title" style="left:0;top:3476px;width:1200px;text-align:center;font-size:38px">Affordable Price Plans</h2>

  <div class="price-card" style="left:125px">
    <div class="price-head"><strong>$45.99</strong><span>/month</span></div>
    <ul>
      <li><span class="tick"><svg width="12" height="10" viewBox="0 0 12 10"><path d="M1 5l3 3 7-7" stroke="#6fb52c" stroke-width="1.8" fill="none"/></svg></span>Lorem ipsum dolor sit</li>
      <li><span class="tick"><svg width="12" height="10" viewBox="0 0 12 10"><path d="M1 5l3 3 7-7" stroke="#6fb52c" stroke-width="1.8" fill="none"/></svg></span>Lorem ipsum dolor sit</li>
      <li><span class="tick"><svg width="12" height="10" viewBox="0 0 12 10"><path d="M1 5l3 3 7-7" stroke="#6fb52c" stroke-width="1.8" fill="none"/></svg></span>Lorem ipsum dolor sit</li>
      <li><span class="tick"><svg width="12" height="10" viewBox="0 0 12 10"><path d="M1 5l3 3 7-7" stroke="#6fb52c" stroke-width="1.8" fill="none"/></svg></span>Lorem ipsum dolor sit</li>
    </ul>
    <a class="pill" href="#">GET STARTED</a>
  </div>
  <div class="price-card featured" style="left:454px">
    <div class="price-head"><strong>$55.99</strong><span>/month</span></div>
    <ul style="padding-top:16px">
      <li><span class="tick"><svg width="12" height="10" viewBox="0 0 12 10"><path d="M1 5l3 3 7-7" stroke="#fff" stroke-width="1.8" fill="none"/></svg></span>Lorem ipsum dolor sit</li>
      <li><span class="tick"><svg width="12" height="10" viewBox="0 0 12 10"><path d="M1 5l3 3 7-7" stroke="#fff" stroke-width="1.8" fill="none"/></svg></span>Lorem ipsum dolor sit</li>
      <li><span class="tick"><svg width="12" height="10" viewBox="0 0 12 10"><path d="M1 5l3 3 7-7" stroke="#fff" stroke-width="1.8" fill="none"/></svg></span>Lorem ipsum dolor sit</li>
      <li><span class="tick"><svg width="10" height="10" viewBox="0 0 10 10"><path d="M2 2l6 6M8 2l-6 6" stroke="#fff" stroke-width="1.6"/></svg></span>Lorem ipsum dolor sit</li>
    </ul>
    <a class="pill" href="#">GET STARTED</a>
  </div>
  <div class="price-card" style="left:778px">
    <div class="price-head"><strong>$99.99</strong><span>/month</span></div>
    <ul>
      <li><span class="tick"><svg width="12" height="10" viewBox="0 0 12 10"><path d="M1 5l3 3 7-7" stroke="#6fb52c" stroke-width="1.8" fill="none"/></svg></span>Lorem ipsum dolor sit</li>
      <li><span class="tick"><svg width="12" height="10" viewBox="0 0 12 10"><path d="M1 5l3 3 7-7" stroke="#6fb52c" stroke-width="1.8" fill="none"/></svg></span>Lorem ipsum dolor sit</li>
      <li><span class="tick"><svg width="12" height="10" viewBox="0 0 12 10"><path d="M1 5l3 3 7-7" stroke="#6fb52c" stroke-width="1.8" fill="none"/></svg></span>Lorem ipsum dolor sit</li>
      <li><span class="tick"><svg width="12" height="10" viewBox="0 0 12 10"><path d="M1 5l3 3 7-7" stroke="#6fb52c" stroke-width="1.8" fill="none"/></svg></span>Lorem ipsum dolor sit</li>
    </ul>
    <a class="pill" href="#">GET STARTED</a>
  </div>
</section>

<section>
  <div class="contact-copy">
    <div class="eyebrow">Get In Touch <span class="rule"></span></div>
    <h2>Contact Lumen Grove</h2>
    <p class="lead">Lorem ipsum dolor sit amet, consectetur adipiscing elit. Nunc et urna ut libero dignissim faucibus a sit amet sapien.</p>
  </div>
  <div class="field" style="left:130px;top:4300px;width:200px">First Name:</div>
  <div class="field" style="left:348px;top:4300px;width:198px">Last Name:</div>
  <div class="field" style="left:130px;top:4358px;width:200px">Phone:</div>
  <div class="field" style="left:348px;top:4358px;width:198px">Email:</div>
  <div class="field" style="left:130px;top:4418px;width:416px;height:84px">Message:</div>
  <a class="abs pill" href="#" style="left:130px;top:4530px;height:44px;padding:0 8px 0 22px;font-size:12px">SUBMIT NOW <span class="arrow-dot"><svg width="10" height="10" viewBox="0 0 10 10"><path d="M3 2l3 3-3 3" stroke="#6fb52c" stroke-width="1.8" fill="none"/></svg></span></a>
  <div class="dot-grid">
    <span></span><span></span><span></span><span></span><span></span><span></span>
    <span class="off"></span><span class="off"></span><span></span><span></span><span></span><span></span>
    <span class="off"></span><span class="off"></span><span class="off"></span><span></span><span></span><span></span>
    <span class="off"></span><span class="off"></span><span class="off"></span><span class="off"></span><span></span><span></span>
    <span class="off"></span><span class="off"></span><span class="off"></span><span class="off"></span><span></span><span></span>
    <span class="off"></span><span class="off"></span><span class="off"></span><span class="off"></span><span></span><span></span>
  </div>
  <div class="contact-media" role="img" aria-label="Silhouetted person standing before a glowing server room display"></div>
</section>

<footer class="site-footer">
  <div class="f-line" style="left:68px;top:122px;width:414px"></div>
  <div class="f-line" style="left:718px;top:122px;width:416px"></div>
  <div class="f-line" style="left:68px;top:220px;width:414px"></div>
  <div class="f-line" style="left:718px;top:220px;width:416px"></div>
  <nav class="f-links" style="left:140px;top:160px"><a href="#">HOW IT WORKS</a><span class="bullet"></span><a href="#">PRODUCTS</a></nav>
  <div class="f-brand">Lumen Grove</div>
  <nav class="f-links" style="left:850px;top:160px"><a href="#">PRICING</a><span class="bullet"></span><a href="#">CONTACT US</a></nav>
  <div class="f-contacts">
    <div class="f-item"><span class="f-icon"><svg width="30" height="30" viewBox="0 0 24 24"><path d="M6.6 10.8a15 15 0 0 0 6.6 6.6l2.2-2.2c.3-.3.7-.4 1-.2 1.1.4 2.3.6 3.6.6.6 0 1 .4 1 1V20c0 .6-.4 1-1 1A17 17 0 0 1 3 4c0-.6.4-1 1-1h3.5c.6 0 1 .4 1 1 0 1.3.2 2.5.6 3.6.1.3 0 .7-.2 1z" fill="#000"/></svg></span><div><b>CALL US</b><small>8012 555 0142</small></div></div>
    <div class="f-item" style="width:260px"><span class="f-icon"><svg width="30" height="24" viewBox="0 0 30 24"><rect x="2" y="3" width="26" height="18" fill="none" stroke="#000" stroke-width="2.4"/><path d="M2 3l13 10L28 3" fill="none" stroke="#000" stroke-width="2.4"/></svg></span><div><b>EMAIL US</b><small>info@lumengrove.example</small></div></div>
    <div class="f-item"><span class="f-icon"><svg width="24" height="32" viewBox="0 0 24 32"><path d="M12 1a11 11 0 0 0-11 11c0 8 11 19 11 19s11-11 11-19A11 11 0 0 0 12 1z" fill="#000"/><circle cx="12" cy="12" r="4" fill="#fff"/></svg></span><div><b>LOCATION 1</b><small>Address line dummy here</small></div></div>
    <div class="f-item"><span class="f-icon"><svg width="24" height="32" viewBox="0 0 24 32"><path d="M12 1a11 11 0 0 0-11 11c0 8 11 19 11 19s11-11 11-19A11 11 0 0 0 12 1z" fill="#000"/><circle cx="12" cy="12" r="4" fill="#fff"/></svg></span><div><b>LOCATION 2</b><small>Address line dummy here</small></div></div>
  </div>
  <div class="f-line" style="left:68px;top:376px;width:1066px"></div>
  <p class="copyright">Copyright © 2024 All Rights Reserved By Company Name</p>
  <a class="to-top" href="#"><svg width="12" height="12" viewBox="0 0 12 12"><path d="M2 8l4-4 4 4" stroke="#000" stroke-width="2" fill="none"/></svg></a>
</footer>

</body>
</html>
```